Need someone to design a book cover for a book called The Copper Tide. The layout needs to be on a 5"x 8" with a 0.75" spine and a 1/8" bleed.

I would like the background of the cover to include the columns from the temple of Argent Heron in Athens (kiones argyrou erodiou).

The book is a psychological sexual thriller taking place in modern Athens during a financial crisis.

Please leave a text placeholder on the back of the cover.

```html
<!DOCTYPE html>
<html lang="en">
<head>
<meta charset="utf-8">
<title>The Copper Tide – Book Cover</title>
<link rel="stylesheet" href="https://fonts.googleapis.com/css2?family=Quicksand:wght@400;500;600&family=Dancing+Script:wght@600&display=swap">
<style>
  :root {
    --page: #e6e6e6;
    --back-ink: #000000;
    --title-white: #ffffff;
    --body-grey: #8c8c8c;
    --ember-dark: #5a0e06;
    --ember-red: #b3200f;
    --ember-orange: #d9550f;
    --ember-amber: #ee8a1c;
    --ember-violet: #8a4a6e;
  }
  * { box-sizing: border-box; margin: 0; padding: 0; }
  html, body {
    width: 1200px; height: 1200px; overflow: hidden;
    background: var(--page);
  }
  .spread {
    position: relative; width: 1200px; height: 1200px;
  }
  .cover {
    position: absolute; top: 200px; width: 500px; height: 800px;
    overflow: hidden;
  }
  .cover--back {
    left: 70px; background: var(--back-ink);
    padding: 0 40px;
  }
  .cover--front { left: 630px; }

  .title {
    font-family: "Quicksand", sans-serif; font-weight: 500;
    color: var(--title-white); text-align: center; line-height: 1;
    letter-spacing: -0.01em;
  }
  .title__article { display: block; }
  .title__word { display: block; }

  .cover--back .title { margin-top: 100px; }
  .cover--back .title__article { font-size: 26px; margin-bottom: 6px; }
  .cover--back .title__word { font-size: 42px; margin-bottom: 6px; }

  .blurb {
    font-family: "Quicksand", sans-serif; font-weight: 500;
    font-size: 14px; line-height: 1.22; color: var(--body-grey);
    text-align: justify; margin-top: 34px;
  }
  .blurb + .blurb { margin-top: 46px; }
  .blurb--last { text-align: left; }

  .signature {
    font-family: "Dancing Script", cursive; font-weight: 600;
    font-size: 26px; color: var(--title-white);
    position: absolute; right: 90px; bottom: 104px;
  }

  .cover-art {
    position: absolute; inset: 0;
    background:
      radial-gradient(ellipse 60% 35% at 70% 70%, rgba(238,138,28,0.55), transparent 70%),
      linear-gradient(135deg, var(--ember-red) 0%, var(--ember-dark) 22%, var(--ember-orange) 48%, var(--ember-amber) 70%, var(--ember-orange) 88%, var(--ember-violet) 100%);
  }
  .cover--front .title {
    position: absolute; left: 100px; width: 340px; top: 330px;
  }
  .cover--front .title__article { font-size: 40px; margin-bottom: 8px; }
  .cover--front .title__word { font-size: 66px; margin-bottom: 10px; }
  .author {
    position: absolute; left: 0; right: 0; bottom: 46px;
    padding-left: 80px;
    font-family: "Quicksand", sans-serif; font-weight: 500;
    font-size: 22px; color: var(--title-white); text-align: center;
  }
</style>
</head>
<body>
<main class="spread">
  <section class="cover cover--back" aria-label="Back cover">
    <h2 class="title">
      <span class="title__article">THE</span>
      <span class="title__word">COPPER</span>
      <span class="title__word">TIDE</span>
    </h2>
    <p class="blurb">Lorem Ipsum is simply dummy text of the printing and typesetting industry. Lorem Ipsum has been the industry's standard dummy text ever since the 1500s, when an unknown printer took a galley of type and scrambled it to make a type specimen book. It has survived not only five centuries, but also the leap into electronic typesetting, remaining essentially unchanged. It was popularised in the 1960s with the release of Lettrafix sheets containing Lorem Ipsum passages, and more recently with desktop publishing software like Quillset PageForge including versions of Lorem Ipsum.</p>
    <p class="blurb">Lorem Ipsum is simply dummy text of the printing and typesetting industry. Lorem Ipsum has been the industry's standard dummy text ever since the 1500s, when an unknown printer took a galley of type and scrambled it to make a type specimen book.</p>
    <p class="blurb blurb--last">It has survived not only five centuries, but also the leap into electronic typesetting, remaining essentially unchanged.</p>
    <p class="signature">Author Name</p>
  </section>

  <section class="cover cover--front" aria-label="Front cover">
    <div class="cover-art" role="img" aria-label="Grunge red and orange photo-collage of the columns of the temple of Argent Heron in Athens with red arrows and reclining figures"></div>
    <h1 class="title">
      <span class="title__article">THE</span>
      <span class="title__word">COPPER</span>
      <span class="title__word">TIDE</span>
    </h1>
    <p class="author">AUTHOR NAME</p>
  </section>
</main>
</body>
</html>
```